Company director needs a business card design

I am a semi-retired former senior finance executive who sits on a number of public and private company boards and do some consulting work. I work largely with emerging businesses but deal regularly with top end of town lawyers, bankers etc. I need a thoughtful but relatively conservative design which would also resonate with my younger client base. Some colour would be good. Information limited to name, address, office tel, mobile and email.

Industry/Entity Type

Finance

```html
<!DOCTYPE html>
<html lang="en">
<head>
<meta charset="utf-8">
<title>Daniel Whitmore — Business Card Concepts</title>
<link rel="stylesheet" href="https://fonts.googleapis.com/css2?family=Josefin+Sans:wght@400;600&family=Montserrat:wght@500&family=Poiret+One&family=Arimo:wght@400;700&display=swap">
<style>
  :root {
    --bronze: #a57a50;
    --bronze-dark: #6e4d2f;
    --navy: #383a4f;
    --blush: #ecccd6;
    --mint: #c3e6dc;
    --sand: #c4b199;
    --slate: #5e5e5e;
    --rose: #c19483;
    --grey: #808080;
    --grey-ink: #555555;
    --ink: #000000;
    --paper: #ffffff;
    --page: #ffffff;
  }
  * { margin: 0; padding: 0; box-sizing: border-box; }
  html, body { width: 1200px; height: 900px; overflow: hidden; background: var(--page); }
  .sheet { position: relative; width: 1200px; height: 900px; font-family: "Arimo", Arial, sans-serif; }
  .card { position: absolute; overflow: hidden; box-shadow: 4px 5px 6px rgba(0,0,0,.45); }
  .card > * { position: absolute; white-space: nowrap; }
  .name { font-family: "Josefin Sans", sans-serif; font-weight: 600; }
  .detail { font-size: 8.5px; }
  .card > .center, .card > .detail.center { left: 0; right: 0; text-align: center; }
  .mark { font-family: "Josefin Sans", sans-serif; font-weight: 600; font-size: 9px; letter-spacing: 2px; }

  /* Card 1 — bronze frame */
  .card--bronze { left: 20px; top: 20px; width: 225px; height: 393px; background: var(--bronze); }
  .card--bronze .panel { left: 7px; top: 2px; width: 210px; height: 310px; background: var(--paper); }
  .card--bronze .name { left: 22px; top: 44px; font-size: 18px; color: var(--bronze); }
  .card--bronze .rule { left: 22px; top: 76px; width: 180px; height: 3px; background: var(--bronze); }
  .card--bronze .detail { left: 11px; font-size: 10px; color: var(--bronze-dark); }

  /* Card 2 — navy */
  .card--navy { left: 285px; top: 20px; width: 225px; height: 393px; background: var(--navy); color: var(--blush); }
  .card--navy .frame { left: 14px; top: 55px; width: 197px; height: 48px; border: 2px solid var(--blush); display: flex; align-items: center; justify-content: center; }
  .card--navy .name { font-size: 13.5px; letter-spacing: 2px; }
  .card--navy .rule { left: 47px; top: 204px; width: 132px; height: 3px; background: var(--blush); }
  .card--navy .detail { left: 38px; }

  /* Card 3 — mint */
  .card--mint { left: 565px; top: 22px; width: 225px; height: 392px; background: var(--mint); color: var(--ink); }
  .card--mint .frame { left: 25px; top: 102px; width: 174px; height: 168px; border: 5px solid var(--ink); display: flex; align-items: center; justify-content: center; padding-top: 40px; }
  .card--mint .name { font-family: "Montserrat", sans-serif; font-weight: 500; font-size: 14.5px; }
  .card--mint .detail { left: 45px; }

  /* Card 4 — sand */
  .card--sand { left: 809px; top: 22px; width: 223px; height: 392px; background: var(--sand); color: var(--slate); }
  .card--sand .name { left: 7px; top: 261px; font-family: "Arimo", sans-serif; font-weight: 700; font-size: 18px; }
  .card--sand .rule { left: 7px; top: 289px; width: 174px; height: 3px; background: var(--slate); }
  .card--sand .detail { left: 7px; }
  .card--sand .bold { font-weight: 700; }

  /* Card 5 — rose */
  .card--rose { left: 20px; top: 443px; width: 197px; height: 347px; background: var(--rose); color: var(--paper); }
  .card--rose .name { top: 65px; font-size: 15.5px; font-weight: 400; }
  .card--rose .bar { left: 97px; top: 105px; width: 9px; height: 55px; background: var(--paper); }
  .card--rose .detail { font-size: 8px; }

  /* Card 6 — white framed */
  .card--framed { left: 254px; top: 443px; width: 197px; height: 347px; background: var(--paper); color: var(--ink); }
  .card--framed .frame { left: 11px; top: 46px; width: 174px; height: 44px; border: 4px solid var(--ink); display: flex; align-items: center; justify-content: center; }
  .card--framed .name { font-size: 12.5px; letter-spacing: 2px; }
  .card--framed .rule { left: 41px; top: 180px; width: 116px; height: 4px; background: var(--ink); }
  .card--framed .detail { left: 34px; }

  /* Card 7 — landscape, bronze tab */
  .card--tab { left: 488px; top: 452px; width: 317px; height: 182px; background: var(--paper); color: var(--bronze); }
  .card--tab .name { left: 7px; top: 136px; font-size: 11px; }
  .card--tab .band { left: 172px; top: 144px; width: 145px; height: 7px; background: var(--bronze); }
  .card--tab .detail { font-size: 6.5px; }
  .card--tab .bold { font-weight: 700; color: var(--bronze-dark); }

  /* Card 8 — landscape, bronze footer */
  .card--footer { left: 488px; top: 659px; width: 317px; height: 180px; background: var(--paper); color: var(--bronze); }
  .card--footer .name { left: 10px; top: 16px; font-size: 11px; }
  .card--footer .rule { left: 10px; top: 29px; width: 108px; height: 1.5px; background: var(--bronze); }
  .card--footer .detail { font-size: 6.5px; }
  .card--footer .band { left: 0; bottom: 0; width: 317px; height: 14px; background: var(--bronze); color: var(--paper); font-weight: 700; font-size: 6.5px; }
  .card--footer .band span { position: absolute; top: 3px; }

  /* Card 9 — grey */
  .card--grey { left: 837px; top: 452px; width: 333px; height: 188px; background: var(--grey); color: var(--grey-ink); }
  .card--grey .name { top: 78px; font-family: "Poiret One", sans-serif; font-weight: 400; font-size: 15px; letter-spacing: 1px; }
  .card--grey .detail { font-size: 7px; }
  .card--grey .bold { font-weight: 700; }

  /* Card 10 — white with grey bars */
  .card--bars { left: 837px; top: 651px; width: 333px; height: 188px; background: var(--paper); color: var(--grey-ink); }
  .card--bars .tick { left: 325px; top: 13px; width: 8px; height: 30px; background: var(--grey); }
  .card--bars .name { left: 14px; top: 90px; font-family: "Poiret One", sans-serif; font-weight: 400; font-size: 14px; color: #7a7a7a; letter-spacing: 0.5px; }
  .card--bars .bar { left: 159px; top: 89px; width: 8px; height: 87px; background: var(--grey); }
  .card--bars .detail { left: 181px; font-size: 7px; }
  .card--bars .bold { font-weight: 700; }
</style>
</head>
<body>
<main class="sheet">

  <section class="card card--bronze">
    <div class="panel"></div>
    <h1 class="name">DANIEL WHITMORE</h1>
    <div class="rule"></div>
    <p class="detail" style="top:326px">48 Larkspur Road, Seabrook NSW 2090</p>
    <p class="detail" style="top:344px">email: daniel_whitmore@mailbox.net.au</p>
    <p class="detail" style="top:365px">tel:02 9555 0142 mob:0400 555 271</p>
  </section>

  <section class="card card--navy">
    <div class="frame"><span class="name">DANIEL WHITMORE</span></div>
    <p class="detail center" style="top:162px">48 Larkspur Road, Seabrook NSW 2090</p>
    <div class="rule"></div>
    <p class="detail" style="top:240px">email: daniel_whitmore@mailbox.net.au</p>
    <p class="detail" style="top:256px">tel:02 9555 0142&nbsp;&nbsp;&nbsp; mob:0400 555 271</p>
    <p class="mark center" style="top:357px">WHITMORE</p>
  </section>

  <section class="card card--mint">
    <div class="frame"><span class="name">DANIEL WHITMORE</span></div>
    <p class="detail center" style="top:286px">48 Larkspur Road, Seabrook NSW 2090</p>
    <p class="detail" style="top:325px">email: daniel_whitmore@mailbox.net.au</p>
    <p class="detail" style="top:343px">tel:02 9555 0142&nbsp;&nbsp;&nbsp; mob:0400 555 271</p>
  </section>

  <section class="card card--sand">
    <p class="mark center" style="top:40px">WHITMORE</p>
    <h1 class="name">DANIEL WHITMORE</h1>
    <div class="rule"></div>
    <p class="detail" style="top:301px">48 Larkspur Road, Seabrook NSW 2090</p>
    <p class="detail" style="top:342px">email: daniel_whitmore@mailbox.net.au</p>
    <p class="detail bold" style="top:356px">tel:02 9555 0142&nbsp;&nbsp;&nbsp;&nbsp;&nbsp;&nbsp; mob:0400 555 271</p>
  </section>

  <section class="card card--rose">
    <h1 class="name center">DANIEL WHITMORE</h1>
    <div class="bar"></div>
    <p class="detail center" style="top:277px">48 Larkspur Road, Seabrook NSW 2090</p>
    <p class="detail" style="top:304px;left:38px">email: daniel_whitmore@mailbox.net.au</p>
    <p class="detail" style="top:319px;left:38px">tel:02 9555 0142&nbsp;&nbsp; mob:0400 555 271</p>
  </section>

  <section class="card card--framed">
    <div class="frame"><span class="name">DANIEL WHITMORE</span></div>
    <p class="detail center" style="top:142px">48 Larkspur Road, Seabrook NSW 2090</p>
    <div class="rule"></div>
    <p class="detail" style="top:210px">email: daniel_whitmore@mailbox.net.au</p>
    <p class="detail" style="top:226px">tel:02 9555 0142 mob:0400 555 271</p>
    <p class="mark center" style="top:314px">WHITMORE</p>
  </section>

  <section class="card card--tab">
    <h1 class="name">DANIEL WHITMORE</h1>
    <p class="detail" style="top:152px;left:7px">48 Larkspur Road, Seabrook NSW 2090</p>
    <div class="band"></div>
    <p class="detail bold" style="top:154px;right:8px">email: daniel_whitmore@mailbox.net.au</p>
    <p class="detail bold" style="top:168px;left:177px">tel:02 9555 0142&nbsp;&nbsp;&nbsp;&nbsp;&nbsp;&nbsp; mob:0400 555 271</p>
  </section>

  <section class="card card--footer">
    <h1 class="name">DANIEL WHITMORE</h1>
    <div class="rule"></div>
    <p class="detail" style="top:36px;left:10px">48 Larkspur Road, Seabrook NSW 2090</p>
    <div class="band">
      <span style="left:10px">email: daniel_whitmore@mailbox.net.au</span>
      <span style="left:184px">tel:02 9555 0142</span>
      <span style="left:250px">mob:0400 555 271</span>
    </div>
  </section>

  <section class="card card--grey">
    <h1 class="name center">DANIEL WHITMORE</h1>
    <p class="detail" style="top:159px;left:14px">48 Larkspur Road, Seabrook NSW 2090</p>
    <p class="detail bold" style="top:152px;right:12px">email: daniel_whitmore@mailbox.net.au</p>
    <p class="detail bold" style="top:167px;left:198px">tel:02 9555 0142&nbsp;&nbsp;&nbsp;&nbsp;&nbsp;&nbsp; mob:0400 555 271</p>
  </section>

  <section class="card card--bars">
    <div class="tick"></div>
    <h1 class="name">DANIEL WHITMORE</h1>
    <div class="bar"></div>
    <p class="detail" style="top:106px">48 Larkspur Road, Seabrook NSW 2090</p>
    <p class="detail" style="top:129px">email: daniel_whitmore@mailbox.net.au</p>
    <p class="detail bold" style="top:144px">tel:02 9555 0142&nbsp;&nbsp;&nbsp;&nbsp;&nbsp;&nbsp; mob:0400 555 271</p>
  </section>

</main>
</body>
</html>
```